Zielgruppe
Wir sind ein Personaldienstleister und vermitteln ausländisches medizinisches Fachpersonal an deutsche Einrichtungen. Unsere Zielgruppe sind Krankenhäuser, Pflegeheime, Ärztehäuser, Praxen, Labore und weitere medizinische Institutionen.
Aufgabenstellung
Wir haben eine Infobroschüre sowie eine PowerPoint Präsentation bereits mit einem groben Design erstellt. Texte und Beispielbilder (Stockmaterial) sind ebenfalls vorhanden, gerne wünschen wir uns auch Eigeninitiative bei der Wahl der Bilder passend zum neuen Design.
Wir wünschen uns ein Redesign mit einem kreativen, einzigartigen Design. Zudem ist uns wichtig, dass unsere Infografiken qualitativ und hochwertig gestaltet werden.
Dieses Projekt ist mit zukünftigen Folgeprojekten verbunden, da wir weitere Präsentationen und Broschüren für andere Zielgruppen benötigen.

```html
<!DOCTYPE html>
<html lang="de">
<head>
<meta charset="utf-8">
<title>Velmora HR – Infobroschüre</title>
<link href="https://fonts.googleapis.com/css2?family=Roboto:wght@400;500;700&display=swap" rel="stylesheet">
<style>
  :root{
    --stage:#939393;
    --paper:#ffffff;
    --teal-dark:#1b4148;
    --teal-mid:#24525a;
    --teal-green:#3b8a70;
    --mint:#c9e4da;
    --line-grey:#c9c9c9;
    --text:#3d4447;
  }
  *{margin:0;padding:0;box-sizing:border-box}
  html,body{width:917px;height:1200px;overflow:hidden}
  body{background:var(--stage);font-family:'Roboto',sans-serif;color:var(--text);position:relative}
  .page{position:absolute;width:389px;height:548px;background:var(--paper);overflow:hidden}
  .page--process{left:50px;top:31px}
  .page--pricing{left:459px;top:31px}
  .page--steps{left:50px;top:616px}
  .page--cover{left:450px;top:616px}
  .page-title{position:absolute;left:0;width:100%;text-align:center;font-weight:700;color:var(--teal-dark);letter-spacing:-.2px}
  .graphics{position:absolute;left:0;top:0}
  .step-num{position:absolute;font-size:14px;font-weight:500;color:var(--teal-dark);transform:translateY(-50%)}
  .step-text{position:absolute;font-size:4.3px;line-height:1.3;color:var(--text);width:92px}
  .footer-bar{position:absolute;left:4px;right:3px;height:17px;background:var(--teal-dark);display:flex;align-items:center;justify-content:space-around;color:#fff;font-size:6.4px}
  .photo{position:absolute;background:linear-gradient(135deg,#e4e4e2 0%,#d2cec9 50%,#e9e3db 100%)}
  .pricing-panel{position:absolute;left:3px;right:3px;top:228px;bottom:3px;background:var(--teal-dark);color:#fff}
  .pricing-panel h2{position:absolute;left:15px;top:14px;font-size:14.2px;font-weight:700}
  .pricing-copy{position:absolute;left:15px;top:42px;width:350px;font-size:8.1px;line-height:1.25}
  .pricing-copy p{margin-bottom:10px}
  .talentpool{position:absolute;left:9px;right:9px;top:184px;height:120px;background:var(--mint);border-radius:10px;color:var(--teal-dark);text-align:center;padding:8px 6px 0}
  .talentpool h3{font-size:14.2px;font-weight:500;margin-bottom:6px}
  .talentpool p{font-size:7.4px;line-height:1.3}
  .talentpool .more{margin-top:8px}
  .tl-text{position:absolute;font-size:5.6px;line-height:1.22;color:var(--text);text-align:justify}
  .tl-text strong{display:block;color:var(--teal-dark);font-weight:700;text-align:left}
  .first-day h3{position:absolute;left:16px;top:460px;font-size:12px;font-weight:400;color:var(--teal-dark)}
  .first-day p{position:absolute;left:16px;top:482px;width:358px;font-size:6.1px;line-height:1.22}
  .cover-panel{position:absolute;left:4px;top:4px;right:4px;bottom:3px;background:var(--teal-dark)}
  .cover-photo{position:absolute;inset:0;background:linear-gradient(180deg,var(--teal-dark) 0%,var(--teal-mid) 55%,#2c5f7e 100%)}
</style>
</head>
<body>

<section class="page page--process">
  <h1 class="page-title" style="top:17px;font-size:22px">Unser Rekrutierungsverfahren</h1>

  <svg class="graphics" width="389" height="548" viewBox="0 0 389 548">
    <defs>
      <g id="ring">
        <circle r="27" fill="var(--mint)"/>
        <circle r="32" fill="none" stroke="var(--teal-dark)" stroke-width=".7" stroke-dasharray="38 14 30 120" transform="rotate(-110)"/>
      </g>
    </defs>
    <g fill="none" stroke="var(--teal-dark)" stroke-width=".7" stroke-dasharray="2 1.5">
      <path d="M153 74H141V153H158"/>
      <path d="M38 185H25V266H40"/><path d="M150 185H138V266H152"/><path d="M278 185H265V266H282"/>
      <path d="M38 298H25V376H40"/><path d="M152 298H140V376H153"/><path d="M277 298H264V376H279"/>
      <path d="M41 407H28V486H41"/><path d="M153 407H140V486H153"/><path d="M277 407H264V486H279"/>
    </g>
    <g fill="var(--teal-dark)">
      <circle cx="153" cy="74" r="4"/><circle cx="158" cy="153" r="4"/>
      <circle cx="38" cy="185" r="4"/><circle cx="40" cy="266" r="4"/>
      <circle cx="150" cy="185" r="4"/><circle cx="152" cy="266" r="4"/>
      <circle cx="278" cy="185" r="4"/><circle cx="282" cy="266" r="4"/>
      <circle cx="38" cy="298" r="4"/><circle cx="40" cy="376" r="4"/>
      <circle cx="152" cy="298" r="4"/><circle cx="153" cy="376" r="4"/>
      <circle cx="277" cy="298" r="4"/><circle cx="279" cy="376" r="4"/>
      <circle cx="41" cy="407" r="4"/><circle cx="41" cy="486" r="4"/>
      <circle cx="153" cy="407" r="4"/><circle cx="153" cy="486" r="4"/>
      <circle cx="277" cy="407" r="4"/><circle cx="279" cy="486" r="4"/>
    </g>

    <g stroke="var(--teal-dark)" stroke-width="1.4" fill="none" stroke-linecap="round" stroke-linejoin="round">
      <g transform="translate(191 86)"><use href="#ring"/>
        <rect x="-10" y="-13" width="19" height="25" rx="1.5"/><path d="M-6 -7h10M-6 -2h10M-6 3h6M3 10l9-11 2 2-9 11-3 1z"/></g>
      <g transform="translate(76 197)"><use href="#ring"/>
        <path d="M-14 -6a13 9 0 1 1 6 8l-6 4 2-5a9 9 0 0 1-2-7z"/><path d="M4 6a9 6 0 0 0 10 -4l1 9-5-3"/>
        <text x="-5" y="-3" font-size="8" font-family="Roboto,sans-serif" fill="var(--teal-dark)" stroke="none" text-anchor="middle" font-weight="500">DE</text></g>
      <g transform="translate(189 197)"><use href="#ring"/>
        <path d="M-9 -12h10l6 6v18h-16z"/><path d="M-3 -16h10l6 6v18"/><path d="M1 -12v6h6"/></g>
      <g transform="translate(316 197)"><use href="#ring"/>
        <circle cx="-5" cy="-8" r="3"/><circle cx="5" cy="-8" r="3"/><path d="M-11 2a6 6 0 0 1 12 0M-1 2a6 6 0 0 1 12 0"/>
        <path d="M-16 -2v8l10 8M16 -2v8l-10 8"/></g>
      <g transform="translate(76 304)"><use href="#ring"/>
        <path d="M-8 4h16M0 4v9M-14 -2v13M14 -2v13"/><circle cx="-10" cy="-6" r="3"/><circle cx="10" cy="-6" r="3"/>
        <rect x="-3" y="-17" width="9" height="7" rx="1"/></g>
      <g transform="translate(189 304)"><use href="#ring"/>
        <rect x="-10" y="-12" width="19" height="23"/><path d="M-14 -8v23h19"/><path d="M-6 -6h11M-6 -1h11M-6 4h8"/></g>
      <g transform="translate(316 304)"><use href="#ring"/>
        <path d="M-16 0l16-14 16 14M-11 -4v16h22v-16"/><rect x="-3" y="4" width="6" height="8"/><rect x="-3" y="-6" width="6" height="5"/></g>
      <g transform="translate(76 419)"><use href="#ring"/>
        <rect x="-15" y="-2" width="11" height="12" rx="1.5"/><path d="M-12 -2v-4h5v4M-16 13h30"/>
        <circle cx="5" cy="-12" r="3"/><path d="M5 -8l-2 10-4 9M3 2l6 9M4 -5l7 3"/></g>
      <g transform="translate(189 419)"><use href="#ring"/>
        <path d="M-6 -14h12v5h-12z"/><path d="M0 -13v3M-1.5 -11.5h3"/><circle cx="0" cy="-3" r="6"/><path d="M-12 14a12 10 0 0 1 24 0z"/></g>
      <g transform="translate(316 419)"><use href="#ring"/>
        <rect x="-13" y="-13" width="12" height="12"/><rect x="1" y="-13" width="12" height="12"/><rect x="-13" y="1" width="12" height="12"/><rect x="1" y="1" width="12" height="12"/></g>
    </g>
  </svg>

  <span class="step-num" style="left:146px;top:130px">01</span>
  <p class="step-text" style="left:163px;top:123px">Bewerber:in wird auf uns Aufmerksam, füllt unser Bewerbungsformular aus und reicht die nötigen Dokumente ein.</p>

  <span class="step-num" style="left:28px;top:243px">02</span>
  <p class="step-text" style="left:47px;top:234px">Um das erforderliche Sprachniveau B2 zu erreichen, bieten wir Bewerber:innen kostenlose interne Sprachkurse an.</p>
  <span class="step-num" style="left:141px;top:243px">03</span>
  <p class="step-text" style="left:160px;top:234px">Parallel zu ihren sprachlichen Vorbereitungen beginnen die Bewerber:innen mit dem Anerkennungsprozess.</p>
  <span class="step-num" style="left:270px;top:243px">04</span>
  <p class="step-text" style="left:289px;top:234px">Wir bereiten unsere Kandidat:innen auf die bevorstehenden Videointerviews vor und erarbeiten proaktive Lösungen für Situationen, die während des Vorstellungsgesprächs auftreten können.</p>

  <span class="step-num" style="left:29px;top:355px">05</span>
  <p class="step-text" style="left:50px;top:347px">Die Bewerber:innen haben Vorstellungsgespräche mit potenziellen Arbeitgebern aus Deutschland. Wir begleiten Sie dabei.</p>
  <span class="step-num" style="left:142px;top:355px">06</span>
  <p class="step-text" style="left:161px;top:347px">Bei erfolgreicher Einigung kommt es zur Unterzeichnung eines Arbeitsvertrags. Wir kümmern uns um die weiteren Prozessabläufe.</p>
  <span class="step-num" style="left:268px;top:355px">07</span>
  <p class="step-text" style="left:286px;top:347px">Die für die Beschäftigung in Deutschland erforderlichen Dokumente werden von uns erstellt bzw. eingeholt und wir suchen eine Unterkunft in der Nähe des künftigen Arbeitsortes.</p>

  <span class="step-num" style="left:31px;top:471px">08</span>
  <p class="step-text" style="left:50px;top:462px">Einreise Ihres/r neuen Mitarbeiter:in nach Deutschland. Wir organisieren die Abholung vom Flughafen und den Transport zur Unterkunft.</p>
  <span class="step-num" style="left:144px;top:471px">09</span>
  <p class="step-text" style="left:163px;top:462px">Wir bereiten Ihre neue Fachkraft auf den Arbeitsantritt vor und begleiten sie zum ersten Arbeitstag.</p>
  <span class="step-num" style="left:268px;top:471px">10</span>
  <p class="step-text" style="left:286px;top:462px">Unsere Kandidat:innen werden während der gesamten Probe-/Einarbeitungszeit von uns unterstützt und betreut.</p>

  <footer class="footer-bar" style="top:527px">
    <span>+49 211 555 01 230</span><span>hr@velmora.com</span><span>www.velmora-hr.com</span>
  </footer>
</section>

<section class="page page--pricing">
  <div class="photo" style="left:3px;top:3px;width:383px;height:225px" role="img" aria-label="Foto: Geschäftsleute schütteln sich bei einem Gespräch am Konferenztisch die Hände"></div>
  <div class="pricing-panel">
    <h2>Was kostet eine gute und faire Rekrutierung bei uns?</h2>
    <div class="pricing-copy">
      <p>Wir bei Velmora HR legen großen Wert auf Kundenzufriedenheit. Mit unserem 360°-Service decken wir alle wichtigen Serviceleistungen rund um die Rekrutierung von ausländischen Fachkräften ab und bieten Ihnen dadurch noch mehr Flexibilität und Dynamik.</p>
      <p>Bei der Berechnung unserer Preise spielen somit viele Faktoren eine wichtige Rolle und sind stark abhängig vom Leistungsumfang und der Art der Rekrutierung.</p>
      <p>Preisangebote kalkulieren wir individuell und Bedarfsgerecht erst mit einer konkreten und detaillierten Nachfrage.</p>
      <p>Teilen Sie uns jetzt Ihren Personalbedarf mit!</p>
    </div>
    <div class="talentpool">
      <h3>Unser Talentpool</h3>
      <p>Gesundheits- und Krankenpfleger:in I Pflegefachmann /-frau I Pflegefachassistent:in I Altenpfleger:in I Arzt/Ärztin I Hebamme I Anästhesietechnische:r Assistent:in (ATA) I Operationstechnische:r Assistent:in (OTA) I Medizinisch-technische:r Laborassistent:in (MTLA) I Medizinisch-technische:r Radiologieassistentin (MTRA) I Pflegehilfskräfte I Pflegefachassistent:in I Notfallsanitäter:in I Rettungssanitäter:in I Physiotherapeut:innen I</p>
      <p class="more">… und viele weitere medizinische Berufe.</p>
    </div>
  </div>
</section>

<section class="page page--steps">
  <h1 class="page-title" style="top:32px;font-size:17.5px">In 6 Schritten zu Ihrer neuen Fachkraft</h1>

  <svg class="graphics" width="389" height="548" viewBox="0 0 389 548">
    <line x1="197" y1="104" x2="197" y2="418" stroke="var(--line-grey)" stroke-width="6"/>
    <line x1="148" y1="104" x2="304" y2="104" stroke="var(--teal-green)" stroke-width="7"/>
    <circle cx="148" cy="104" r="10" fill="var(--teal-dark)"/>
    <circle cx="304" cy="104" r="15" fill="#fff" stroke="var(--teal-dark)" stroke-width="4"/>
    <line x1="88" y1="166" x2="246" y2="166" stroke="var(--teal-dark)" stroke-width="7"/>
    <circle cx="246" cy="166" r="10" fill="var(--teal-green)"/>
    <circle cx="88" cy="166" r="15" fill="#fff" stroke="var(--teal-green)" stroke-width="4"/>
    <line x1="148" y1="228" x2="304" y2="228" stroke="var(--teal-dark)" stroke-width="7"/>
    <circle cx="148" cy="228" r="10" fill="var(--mint)"/>
    <circle cx="304" cy="228" r="15" fill="#fff" stroke="var(--mint)" stroke-width="4"/>
    <line x1="88" y1="290" x2="246" y2="290" stroke="var(--teal-green)" stroke-width="7"/>
    <circle cx="246" cy="290" r="10" fill="var(--teal-dark)"/>
    <circle cx="88" cy="290" r="15" fill="#fff" stroke="var(--teal-dark)" stroke-width="4"/>
    <line x1="148" y1="352" x2="304" y2="352" stroke="var(--mint)" stroke-width="7"/>
    <circle cx="148" cy="352" r="10" fill="var(--teal-green)"/>
    <circle cx="304" cy="352" r="15" fill="#fff" stroke="var(--teal-green)" stroke-width="4"/>
    <line x1="88" y1="418" x2="246" y2="418" stroke="var(--teal-green)" stroke-width="7"/>
    <circle cx="246" cy="418" r="10" fill="var(--teal-dark)"/>
    <circle cx="88" cy="418" r="15" fill="#fff" stroke="var(--teal-dark)" stroke-width="4"/>

    <g fill="#fff" stroke-width="5">
      <circle cx="197" cy="104" r="24" stroke="var(--teal-dark)"/>
      <circle cx="197" cy="166" r="24" stroke="var(--teal-green)"/>
      <circle cx="197" cy="228" r="24" stroke="var(--mint)"/>
      <circle cx="197" cy="290" r="24" stroke="var(--teal-dark)"/>
      <circle cx="197" cy="352" r="24" stroke="var(--teal-green)"/>
      <circle cx="197" cy="418" r="24" stroke="var(--teal-dark)"/>
    </g>
    <g stroke="var(--teal-dark)" stroke-width="1.3" fill="none" stroke-linecap="round" stroke-linejoin="round">
      <g transform="translate(197 104)"><rect x="-9" y="-11" width="18" height="22" rx="2"/><circle cx="0" cy="-3" r="3"/><path d="M-5 6a5 4 0 0 1 10 0M11 -6v4M11 1v4"/></g>
      <g transform="translate(197 166)"><path d="M-9 -11h11l5 5v17h-16z" fill="var(--teal-dark)"/><path d="M-5 -3h6M-5 2h6" stroke="#fff"/><path d="M3 10l8-9 2 2-8 9z" fill="#fff"/></g>
      <g transform="translate(197 228)"><circle cx="0" cy="-2" r="3"/><circle cx="-7" cy="1" r="2.5"/><circle cx="7" cy="1" r="2.5"/><path d="M-6 10a6 6 0 0 1 12 0M-12 11a5 5 0 0 1 6-5M12 11a5 5 0 0 0-6-5M-2 -11l2 2 4-4"/></g>
      <g transform="translate(197 290)"><path d="M-7 3h14M0 3v8M-11 -2v12M11 -2v12"/><circle cx="-8" cy="-6" r="2.5"/><circle cx="8" cy="-6" r="2.5"/><rect x="-3" y="-13" width="7" height="5" rx="1"/></g>
      <g transform="translate(197 352)"><circle cx="0" cy="0" r="3"/><circle cx="-10" cy="-9" r="2"/><circle cx="10" cy="-9" r="2"/><circle cx="-10" cy="9" r="2"/><circle cx="10" cy="9" r="2"/><path d="M-6 -9h12M-6 9h12M-10 -5v10M10 -5v10" stroke-dasharray="2 1.5"/></g>
      <g transform="translate(197 418)"><path d="M-15 -3l7-5 6 3 6-3 7 5 4 4-9 9-5-4-4 2-8-6z" fill="var(--teal-dark)"/></g>
    </g>
    <g font-family="Roboto,sans-serif" font-size="12" font-weight="500" fill="var(--teal-dark)" text-anchor="middle">
      <text x="304" y="108">1</text><text x="88" y="170">2</text><text x="304" y="232">3</text>
      <text x="88" y="294">4</text><text x="304" y="356">5</text><text x="88" y="422">6</text>
    </g>
  </svg>

  <p class="tl-text" style="left:16px;top:88px;width:100px;text-align:left"><strong>Kontaktaufnahme</strong>Sie nehmen Kontakt zu uns auf und teilen uns Ihren Personalbedarf, sowie spezielle Stellenanforderungen mit.</p>
  <p class="tl-text" style="left:263px;top:153px;width:104px"><strong>Vertragsmodalitäten</strong>Wir setzen uns mit Ihnen zusammen, besprechen die Einzelheiten und klären die Rahmenbedingungen, individuell auf Sie zugeschnitten.</p>
  <p class="tl-text" style="left:16px;top:211px;width:114px"><strong>Kandidatenvorauswahl</strong>Wir lassen Ihnen vorab übersichtliche CV's potenzieller Kandidat:innen zukommen und Sie treffen eine Vorauswahl bzw. teilen uns eventuelle Anpassungswünsche mit.</p>
  <p class="tl-text" style="left:263px;top:276px;width:111px"><strong>Vorstellungsgespräche</strong>Sie führen die Vorstellungsgespräche mit den Kandidat:innen durch. Unsere Expert:innen begleiten Sie dabei als wichtiges Bindeglied, um bei Missverständnissen und Unklarheiten vorzubeugen.</p>
  <p class="tl-text" style="left:16px;top:340px;width:114px"><strong>Finale Personalauswahl</strong>Sie entscheiden sich für Ihre Wunschmitarbeiter:innen - wir stellen Ihnen zusammen mit einer persönlichen Einschätzung zu den jeweiligen Kandidat:innen alle Informationen und Unterlagen in einem übersichtlichen und informativen Bericht zur Verfügung.</p>
  <p class="tl-text" style="left:263px;top:406px;width:104px"><strong>Arbeitsvertrag</strong>Nach Klärung aller wichtigen Modalitäten und Besonderheiten unterschreibt der/die Bewerber:in seinen/ihren Arbeitsvertrag.</p>

  <div class="first-day">
    <h3>Erster Arbeitstag</h3>
    <p>Wir begleiten und betreuen unsere Kandidat:innen über den kompletten Auswahlprozess hinweg bis zum Ende ihrer Probezeit. Nicht selten können wir auch nach der erfolgreichen Vermittlung noch wertvolle Klärungs- und Motivationsarbeit leisten. Außerdem übernehmen wir sowohl Abschlussgespräche, als auch die gesamte Korrespondenz mit allen Bewerber:innen, die am Auswahlverfahren beteiligt waren.</p>
  </div>

  <footer class="footer-bar" style="top:527px">
    <span>+49 211 555 01 230</span><span>hr@velmora.com</span><span>www.velmora-hr.com</span>
  </footer>
</section>

<section class="page page--cover">
  <div class="cover-panel">
    <div class="cover-photo" role="img" aria-label="Foto: Pflegekraft in blauer Dienstkleidung zeigt lächelnd mit beiden Händen zur Seite"></div>
  </div>
</section>

</body>
</html>
```